3.5" x 11" Door Hanger Design - Residential Roofing Company

We are looking for a double-sided door hanger that we can hang on the doors of prospects. This door hanger would have some brief information about our company, a phone number, website, and then the services that we offer. I don't know that it will have enough room for a lot of pictures, but feel free to use those from the marketing brochure if you think it'll work and I can get you the original as needed.
I have uploaded our certifications, logo, and then our current marketing brochure. The design should be cohesive with our marketing brochure, but doesn't have to match it perfectly.
Lastly, attached is the template that we are planning to print off of. This has a tear off portion at the bottom for a business card for a sales rep. The size of the overall door hanger will be 3.5" x 11", with the bottom 2.5" being the tear off business card with the salesman's information. I'll get you the sales reps information during the final design phase, but we will need name, title, phone number, email, business address, business website, list of services, and then the words "AZ ROC 562071" all on that small portion as well so if they tear it off they still have all the info.

```html
<!DOCTYPE html>
<html lang="en">
<head>
<meta charset="utf-8">
<title>Summit Ridge Roofing – Door Hanger</title>
<link href="https://fonts.googleapis.com/css2?family=Montserrat:wght@400;500;600;700;800&display=swap" rel="stylesheet">
<style>
:root{
  --bg:#ededee;
  --dark:#1c1c1e;
  --dark-2:#2a2a2d;
  --orange:#f05a22;
  --orange-2:#ff7a3d;
  --white:#ffffff;
  --muted:#b9b9bd;
  --green:#3aa14a;
  --blue:#2e5aa7;
}
*{box-sizing:border-box;margin:0;padding:0}
html,body{width:668px;height:1200px;overflow:hidden;background:var(--bg);font-family:"Montserrat",Arial,sans-serif;color:var(--white)}
.sheet{position:relative;width:668px;height:1200px}
.hanger{position:absolute;top:150px;width:300px;height:943px;background:var(--dark);overflow:hidden;box-shadow:0 6px 18px rgba(0,0,0,.18)}
.hanger--front{left:20px}
.hanger--back{left:348px}
.label{position:absolute;top:1110px;font-size:15px;font-weight:600;color:#333}
.label--front{left:150px;transform:translateX(-50%)}
.label--back{left:498px;transform:translateX(-50%)}

.head{position:absolute;top:0;left:0;width:100%;height:120px;background:var(--white)}
.door-hole{position:absolute;left:50%;top:22px;width:62px;height:62px;margin-left:-31px;border-radius:50%;background:var(--bg);border:1px solid #d0d0d4}
.door-slit{position:absolute;left:50%;top:84px;width:1px;height:36px;background:#c4c4c8}
.brand{position:absolute;top:10px;left:0;width:100%;display:flex;align-items:center;justify-content:center;gap:6px;font-weight:800;font-size:13px;color:var(--dark);z-index:2}
.brand__mark{width:9px;height:9px;background:var(--orange)}
.hanger--front .brand{top:92px}
.hanger--back .brand{top:10px;color:var(--white)}

.photo{position:absolute;left:0;width:100%}
.photo--house{top:120px;height:250px;background:linear-gradient(180deg,#9fb3c6 0%,#d8dadb 45%,#7b7670 100%);clip-path:polygon(0 0,100% 0,100% 78%,0 100%)}
.photo--crew{top:0;height:390px;background:linear-gradient(180deg,#c9d3dc 0%,#8a7d6d 45%,#3b332c 100%);clip-path:polygon(0 0,100% 0,100% 100%,0 84%)}

.accent{position:absolute;left:0;width:100%}
.headline{position:absolute;left:18px;top:318px;font-weight:700;line-height:1.1}
.headline__line{font-size:24px;display:block}
.headline__key{display:inline-block;background:var(--orange);padding:2px 8px;font-size:26px;font-weight:800;margin:3px 0}
.headline__trust{color:var(--orange);font-weight:800}
.phone-pill{position:absolute;left:18px;top:430px;display:flex;align-items:center;gap:8px;background:var(--orange);border-radius:20px;padding:7px 16px;font-weight:700;font-size:14px}
.section-title{font-weight:700;font-size:12px;color:var(--orange);margin-bottom:8px}
.intro{position:absolute;left:18px;right:18px;top:478px}
.intro p{font-size:8.5px;line-height:1.45;color:var(--muted);margin-bottom:10px}
.ticks{list-style:none}
.ticks li{display:flex;gap:8px;font-size:8.5px;line-height:1.35;color:var(--muted);margin-bottom:7px}
.ticks b{color:var(--white);font-weight:600}
.tick{flex:0 0 14px;height:14px;border-radius:50%;background:var(--orange);display:flex;align-items:center;justify-content:center}
.site{font-size:9px;color:var(--white);font-weight:600;margin-top:4px}

.tearoff{position:absolute;left:0;bottom:0;width:100%;height:214px;background:var(--white);color:var(--dark);border-top:2px dashed #9a9a9e;padding:22px 18px}
.rep__name{font-weight:800;font-size:15px}
.rep__title{font-size:10px;color:var(--orange);font-weight:600;margin-bottom:12px}
.rep__row{display:flex;align-items:center;gap:7px;font-size:9.5px;margin-bottom:6px}
.rep__services{font-size:8px;color:#555;line-height:1.4;margin-top:8px}
.roc{position:absolute;right:18px;bottom:16px;font-weight:700;font-size:9px;color:var(--dark)}

.back-title{position:absolute;left:18px;top:400px;font-weight:800;font-size:21px;line-height:1.15}
.back-body{position:absolute;left:18px;right:18px;top:460px}
.back-body p{font-size:8.5px;line-height:1.45;color:var(--muted);margin-bottom:12px}
.service{display:flex;gap:9px;margin-bottom:10px}
.service h3{font-size:9.5px;font-weight:700;color:var(--orange)}
.service p{font-size:8px;color:var(--muted);margin:2px 0 0;line-height:1.35}
.contact{position:absolute;left:18px;top:710px;right:18px}
.contact h3{font-size:12px;font-weight:700;margin-bottom:8px}
.contact__row{display:flex;align-items:center;gap:8px;font-size:9px;margin-bottom:6px;color:var(--white)}
.badges{position:absolute;left:18px;bottom:30px;display:flex;gap:10px}
.badge{width:38px;height:38px;border-radius:50%}
.badge--green{background:var(--green)}
.badge--blue{background:var(--blue)}
.back-roc{position:absolute;right:18px;bottom:42px;font-size:9px;font-weight:700;color:var(--muted)}
</style>
</head>
<body>
<main class="sheet">

  <!-- FRONT -->
  <section class="hanger hanger--front" aria-label="Door hanger front">
    <div class="head">
      <div class="door-hole"></div>
    </div>
    <div class="brand"><span class="brand__mark"></span>Summit Ridge Roofing</div>
    <div class="photo photo--house" role="img" aria-label="Photo of a modern suburban house with a new roof"></div>
    <svg class="accent" style="top:280px" width="300" height="80" viewBox="0 0 300 80" aria-hidden="true">
      <polygon points="170,20 300,0 300,14 190,32" fill="#f05a22"/>
      <polygon points="0,58 120,40 110,50 0,68" fill="#f05a22"/>
    </svg>
    <h1 class="headline">
      <span class="headline__line">Quality</span>
      <span class="headline__key">Roofing</span>
      <span class="headline__line headline__trust">you can trust</span>
    </h1>
    <div class="phone-pill">
      <svg width="13" height="13" viewBox="0 0 24 24" aria-hidden="true"><path fill="#fff" d="M6.6 10.8a15 15 0 006.6 6.6l2.2-2.2c.3-.3.7-.4 1-.2 1.1.4 2.3.6 3.6.6.6 0 1 .4 1 1V20c0 .6-.4 1-1 1A17 17 0 013 4c0-.6.4-1 1-1h3.5c.6 0 1 .4 1 1 0 1.3.2 2.5.6 3.6.1.3 0 .7-.2 1z"/></svg>
      (555) 204-3178
    </div>
    <div class="intro">
      <div class="section-title">Why Regular Roof Inspections</div>
      <p>Your roof shields everything beneath it. A yearly check finds small issues early, saving you money and keeping your home safe through every season.</p>
      <ul class="ticks">
        <li><span class="tick"><svg width="8" height="8" viewBox="0 0 10 10"><path d="M1 5l3 3 5-6" stroke="#fff" stroke-width="2" fill="none"/></svg></span><span><b>Early Detection</b> – spot leaks and wear before they grow.</span></li>
        <li><span class="tick"><svg width="8" height="8" viewBox="0 0 10 10"><path d="M1 5l3 3 5-6" stroke="#fff" stroke-width="2" fill="none"/></svg></span><span><b>Longer Roof Life</b> – regular care adds years of service.</span></li>
        <li><span class="tick"><svg width="8" height="8" viewBox="0 0 10 10"><path d="M1 5l3 3 5-6" stroke="#fff" stroke-width="2" fill="none"/></svg></span><span><b>Energy Savings</b> – a sound roof keeps heat where it belongs.</span></li>
        <li><span class="tick"><svg width="8" height="8" viewBox="0 0 10 10"><path d="M1 5l3 3 5-6" stroke="#fff" stroke-width="2" fill="none"/></svg></span><span><b>Peace of Mind</b> – know your home is protected.</span></li>
      </ul>
      <div class="site">www.summitridgeroof.com</div>
    </div>
    <div class="tearoff">
      <div class="rep__name">Sales Representative</div>
      <div class="rep__title">Roofing Consultant</div>
      <div class="rep__row">
        <svg width="11" height="11" viewBox="0 0 24 24"><path fill="#f05a22" d="M6.6 10.8a15 15 0 006.6 6.6l2.2-2.2c.3-.3.7-.4 1-.2 1.1.4 2.3.6 3.6.6.6 0 1 .4 1 1V20c0 .6-.4 1-1 1A17 17 0 013 4c0-.6.4-1 1-1h3.5c.6 0 1 .4 1 1 0 1.3.2 2.5.6 3.6.1.3 0 .7-.2 1z"/></svg>(555) 204-3178</div>
      <div class="rep__row">
        <svg width="11" height="11" viewBox="0 0 24 24"><path fill="#f05a22" d="M2 5h20v14H2z"/><path d="M2 5l10 8 10-8" stroke="#fff" stroke-width="2" fill="none"/></svg>hello@summitridgeroof.com</div>
      <div class="rep__row">
        <svg width="11" height="11" viewBox="0 0 24 24"><path fill="#f05a22" d="M12 2a7 7 0 00-7 7c0 5 7 13 7 13s7-8 7-13a7 7 0 00-7-7zm0 9.5A2.5 2.5 0 1112 6a2.5 2.5 0 010 5.5z"/></svg>480 Pinecrest Way, Prescott, AZ 86301</div>
      <div class="rep__services">Roof Repair · Replacement · Inspections · Storm Damage · Gutters</div>
      <div class="roc">AZ ROC 562071</div>
    </div>
  </section>

  <!-- BACK -->
  <section class="hanger hanger--back" aria-label="Door hanger back">
    <div class="photo photo--crew" role="img" aria-label="Photo of a roofing crew working on a shingle roof"></div>
    <div class="brand"><span class="brand__mark"></span>Summit Ridge Roofing</div>
    <svg class="accent" style="top:330px" width="300" height="70" viewBox="0 0 300 70" aria-hidden="true">
      <polygon points="0,20 140,50 130,60 0,34" fill="#f05a22"/>
      <polygon points="210,40 300,22 300,34 225,50" fill="#f05a22"/>
    </svg>
    <h2 class="back-title">Comprehensive<br>Roofing Services</h2>
    <div class="back-body">
      <p>At Summit Ridge Roofing we offer a full range of services to keep your home covered, sound and good-looking for years to come.</p>
      <div class="service"><span class="tick"><svg width="8" height="8" viewBox="0 0 10 10"><path d="M1 5l3 3 5-6" stroke="#fff" stroke-width="2" fill="none"/></svg></span><div><h3>Roof Inspections &amp; Maintenance</h3><p>Keep your roof in peak condition.</p></div></div>
      <div class="service"><span class="tick"><svg width="8" height="8" viewBox="0 0 10 10"><path d="M1 5l3 3 5-6" stroke="#fff" stroke-width="2" fill="none"/></svg></span><div><h3>Roof Repairs</h3><p>Quick fixes for leaks and damage.</p></div></div>
      <div class="service"><span class="tick"><svg width="8" height="8" viewBox="0 0 10 10"><path d="M1 5l3 3 5-6" stroke="#fff" stroke-width="2" fill="none"/></svg></span><div><h3>Roof Installation</h3><p>Quality materials, expert crews.</p></div></div>
      <div class="service"><span class="tick"><svg width="8" height="8" viewBox="0 0 10 10"><path d="M1 5l3 3 5-6" stroke="#fff" stroke-width="2" fill="none"/></svg></span><div><h3>Storm Damage Repair</h3><p>Fast help after wind and hail.</p></div></div>
    </div>
    <div class="contact">
      <h3>Contact us</h3>
      <div class="contact__row"><svg width="11" height="11" viewBox="0 0 24 24"><path fill="#f05a22" d="M12 2a7 7 0 00-7 7c0 5 7 13 7 13s7-8 7-13a7 7 0 00-7-7zm0 9.5A2.5 2.5 0 1112 6a2.5 2.5 0 010 5.5z"/></svg>480 Pinecrest Way, Prescott, AZ 86301</div>
      <div class="contact__row"><svg width="11" height="11" viewBox="0 0 24 24"><path fill="#f05a22" d="M6.6 10.8a15 15 0 006.6 6.6l2.2-2.2c.3-.3.7-.4 1-.2 1.1.4 2.3.6 3.6.6.6 0 1 .4 1 1V20c0 .6-.4 1-1 1A17 17 0 013 4c0-.6.4-1 1-1h3.5c.6 0 1 .4 1 1 0 1.3.2 2.5.6 3.6.1.3 0 .7-.2 1z"/></svg>(555) 204-3178</div>
      <div class="contact__row"><svg width="11" height="11" viewBox="0 0 24 24"><path fill="#f05a22" d="M2 5h20v14H2z"/><path d="M2 5l10 8 10-8" stroke="#1c1c1e" stroke-width="2" fill="none"/></svg>hello@summitridgeroof.com</div>
    </div>
    <div class="badges">
      <div class="badge badge--green" role="img" aria-label="Certification badge"></div>
      <div class="badge badge--blue" role="img" aria-label="Certification badge"></div>
    </div>
    <div class="back-roc">AZ ROC 562071</div>
  </section>

  <div class="label label--front">Front</div>
  <div class="label label--back">Back</div>
</main>
</body>
</html>
```